CyberSecurity Company Website Design

DO NOT CONTACT US OUTSIDE OF PIXELBAZAAR.COM!

A professional 5 page website design for a cyber security and risk management company. We want to portray a serious and professional approach to online security and risk management for businesses. We want the website to be easy to navigate but with a modern style.

The website design pages my partners have reviewed and wish to emulate (without copying, of course ) are:
wrenforge.com, larkhollow.com and brunel.com, Gavromill.com

The attached Zip file contains a very basic outline of the format we are looking for. We want a nice, modern design that reflects cyber security, securing networks, and risk management for business.

Target Market(s)

Large corporations with CyberSecurity Needs

Number of Pages Required

5+ page

Colors
ec1f27
ffffff
0293ce

Requirements
Must have
• The 5 pages we need designed are;
• Home page, Services, About Us, Careers and Contact.

```html
<!DOCTYPE html>
<html lang="en">
<head>
<meta charset="utf-8">
<title>Verolis CyberTech</title>
<link href="https://fonts.googleapis.com/css2?family=Open+Sans:wght@400;600;700&display=swap" rel="stylesheet">
<style>
:root{
  --red:#e3101f;
  --blue:#0293ce;
  --navy:#0a3d6e;
  --glow:rgba(120,210,255,.55);
  --text:#444;
  --nav:#555;
  --footer:#2a2a2a;
  --footer-text:#c8c8c8;
  --white:#fff;
}
*{margin:0;padding:0;box-sizing:border-box}
html,body{width:1200px;height:1144px;overflow:hidden;background:var(--white)}
body{font-family:"Open Sans",sans-serif;color:var(--text);position:relative}
.site-header{position:absolute;top:0;left:0;width:1200px;height:75px;background:var(--white)}
.brand{position:absolute;left:133px;top:23px;display:flex;align-items:center;gap:8px;font-size:22px;font-weight:700;color:var(--red);text-decoration:none}
.brand-mark{width:14px;height:14px;background:var(--red)}
.main-nav{position:absolute;right:132px;top:28px;display:flex;align-items:center;gap:30px;font-size:14.5px}
.main-nav a{color:var(--nav);text-decoration:none}
.main-nav a.active{color:var(--red)}
.nav-phone{display:flex;align-items:center;gap:5px;font-weight:600;color:#222;font-size:15px}
.hero{position:absolute;top:75px;left:0;width:1200px;height:539px;overflow:hidden}
.hero-visual{position:absolute;inset:0;background:
  radial-gradient(circle at 14% 22%,var(--glow) 0,rgba(120,210,255,0) 9%),
  radial-gradient(circle at 24% 72%,rgba(150,225,255,.5) 0,rgba(150,225,255,0) 10%),
  radial-gradient(circle at 40% 50%,rgba(90,190,255,.35) 0,rgba(90,190,255,0) 12%),
  radial-gradient(circle at 55% 85%,rgba(110,205,255,.4) 0,rgba(110,205,255,0) 11%),
  radial-gradient(circle at 68% 78%,rgba(110,205,255,.35) 0,rgba(110,205,255,0) 9%),
  radial-gradient(circle at 94% 34%,rgba(170,235,255,.45) 0,rgba(170,235,255,0) 6%),
  radial-gradient(circle at 78% 52%,rgba(150,225,255,.35) 0,rgba(150,225,255,0) 5%),
  radial-gradient(ellipse at 25% 55%,#1676c0 0%,#0c4e8c 45%,#083a6b 100%);}
.hero-visual::after{content:"";position:absolute;inset:0;background:linear-gradient(90deg,rgba(6,45,95,.25),rgba(20,115,185,.4))}
.hero-title{position:absolute;right:132px;top:220px;transform:translateY(-50%);font-size:47px;font-weight:700;color:var(--white);letter-spacing:.3px;line-height:1}
.slider-arrow{position:absolute;top:255px;width:28px;height:28px;background:#222;display:flex;align-items:center;justify-content:center}
.slider-arrow.prev{left:0}
.slider-arrow.next{right:0}
.welcome{position:absolute;top:686px;left:133px;width:935px}
.welcome h1{font-size:33.5px;font-weight:700;color:var(--red);letter-spacing:-.2px;line-height:1.2}
.welcome-copy{width:560px;margin-top:13px}
.welcome-copy p{font-size:13px;line-height:22.4px;margin-bottom:8px}
.welcome-photo{position:absolute;left:613px;top:8px;width:322px;height:174px;background:
  radial-gradient(circle at 60% 10%,rgba(90,220,255,.5) 0,rgba(90,220,255,0) 18%),
  radial-gradient(circle at 82% 45%,rgba(90,220,255,.45) 0,rgba(90,220,255,0) 15%),
  radial-gradient(circle at 18% 85%,rgba(90,220,255,.4) 0,rgba(90,220,255,0) 16%),
  linear-gradient(135deg,#5d86ab 0%,#0c3f86 35%,#0a2a66 70%,#b79a80 100%)}
.site-footer{position:absolute;top:949px;left:0;width:1200px;height:195px;background:var(--footer);color:var(--footer-text)}
.footer-notch{position:absolute;left:182px;top:0}
.contact-col{position:absolute;top:21px}
.contact-col h3{font-size:18px;font-weight:400;color:var(--white);display:flex;align-items:center;gap:6px}
.contact-col p{font-size:12.5px;margin-top:5px}
.footer-rule{position:absolute;left:133px;top:91px;width:935px;height:1px;background:#4a4a4a}
.footer-brand{position:absolute;left:133px;top:120px;display:flex;align-items:center;gap:6px;font-size:14px;font-weight:700;color:#9a9a9a}
.footer-brand span{width:9px;height:9px;background:#9a9a9a}
.footer-links{position:absolute;left:250px;top:118px;font-size:12.5px}
.footer-links a{color:var(--footer-text);text-decoration:none}
.footer-links .sep{margin:0 10px}
.copyright{position:absolute;left:250px;top:147px;font-size:12.5px}
.social{position:absolute;right:133px;top:136px;display:flex;gap:22px}
.social span{width:14px;height:14px;border-radius:50%;background:#bdbdbd}
</style>
</head>
<body>
<header class="site-header">
  <a class="brand" href="#"><span class="brand-mark"></span>Verolis</a>
  <nav class="main-nav">
    <a class="active" href="#">Home</a>
    <a href="#">Services</a>
    <a href="#">About Us</a>
    <a href="#">Careers</a>
    <a href="#">Contact</a>
    <span class="nav-phone"><svg width="13" height="13" viewBox="0 0 24 24"><path fill="#222" d="M6.6 10.8c1.4 2.8 3.8 5.1 6.6 6.6l2.2-2.2c.3-.3.7-.4 1-.2 1.1.4 2.3.6 3.6.6.6 0 1 .4 1 1V20c0 .6-.4 1-1 1C10.6 21 3 13.4 3 4c0-.6.4-1 1-1h3.5c.6 0 1 .4 1 1 0 1.3.2 2.5.6 3.6.1.3 0 .7-.2 1z"/></svg>555 218 4730</span>
  </nav>
</header>

<section class="hero">
  <div class="hero-visual" role="img" aria-label="Glowing blue hexagonal network with padlock icons representing secured connections"></div>
  <h2 class="hero-title">Safe • Safer • Verolis</h2>
  <a class="slider-arrow prev" href="#" aria-label="Previous slide"><svg width="14" height="14" viewBox="0 0 14 14"><path d="M12 7H3M7 2.5L2.5 7 7 11.5" stroke="#fff" stroke-width="2.2" fill="none"/></svg></a>
  <a class="slider-arrow next" href="#" aria-label="Next slide"><svg width="14" height="14" viewBox="0 0 14 14"><path d="M2 7h9M7 2.5L11.5 7 7 11.5" stroke="#fff" stroke-width="2.2" fill="none"/></svg></a>
</section>

<section class="welcome">
  <h1>Welcome to Verolis CyberTech (VCT)</h1>
  <div class="welcome-copy">
    <p>We provide advanced security engineering and cybersecurity architecture solutions for the commercial sector and federal government.</p>
    <p>Our security experts create customized IT solutions for private organizations that meet compliance requirements as well required federaland commercial qualifications</p>
    <p>It's all about YOU, our customer, your needs and your safety.</p>
  </div>
  <div class="welcome-photo" role="img" aria-label="Laptop, tablet and phone on a desk showing glowing shield security icons"></div>
</section>

<footer class="site-footer">
  <svg class="footer-notch" width="47" height="43" viewBox="0 0 47 43"><path d="M0 0h47L23.5 43z" fill="#fff"/></svg>
  <div class="contact-col" style="left:252px">
    <h3><svg width="10" height="14" viewBox="0 0 10 14"><path d="M5 0a5 5 0 0 0-5 5c0 3.8 5 9 5 9s5-5.2 5-9a5 5 0 0 0-5-5zm0 7a2 2 0 1 1 0-4 2 2 0 0 1 0 4z" fill="#fff"/></svg>Verolis Corporate Office</h3>
    <p>24 Building name, Harbor Square, City Zipcode</p>
  </div>
  <div class="contact-col" style="left:623px">
    <h3><svg width="13" height="13" viewBox="0 0 24 24"><path fill="#fff" d="M6.6 10.8c1.4 2.8 3.8 5.1 6.6 6.6l2.2-2.2c.3-.3.7-.4 1-.2 1.1.4 2.3.6 3.6.6.6 0 1 .4 1 1V20c0 .6-.4 1-1 1C10.6 21 3 13.4 3 4c0-.6.4-1 1-1h3.5c.6 0 1 .4 1 1 0 1.3.2 2.5.6 3.6.1.3 0 .7-.2 1z"/></svg>Corporate Office</h3>
    <p>Phone : 555 240 1193 &nbsp;/ &nbsp; Fax : 555 376 9021</p>
  </div>
  <div class="contact-col" style="left:967px">
    <h3><svg width="16" height="12" viewBox="0 0 16 12" style="margin-right:4px"><rect width="16" height="12" rx="1" fill="#fff"/><path d="M1 1.5l7 5 7-5" stroke="#2a2a2a" stroke-width="1.4" fill="none"/></svg>Email</h3>
    <p>info@verolis.com</p>
  </div>
  <div class="footer-rule"></div>
  <div class="footer-brand"><span></span>Verolis</div>
  <nav class="footer-links">
    <a href="#">Home</a><span class="sep">|</span><a href="#">Services</a><span class="sep">|</span><a href="#">About Us</a><span class="sep">|</span><a href="#">Careers</a><span class="sep">|</span><a href="#">Contact</a>
  </nav>
  <p class="copyright">Copyright &nbsp;© &nbsp;2018 &nbsp;Verolis. &nbsp;Al rights reserved.</p>
  <div class="social" aria-label="Social links"><span></span><span></span><span></span></div>
</footer>
</body>
</html>
```